Research and Development Technical Training for Process Engineering

We are creating a LearnPoint site that will contain links to several training materials. I will create and upload the content, just looking for graphics and a basic layout for a single homepage. The page should contain unique graphics for the following topics/categories: Methodology, Equipment Training, Design References, Safety & Environmental, and Technology. (See attached example. Layout example DOES NOT need to be followed, only an example).
Also, a graphic to be used for a Powerpoint template that is cohesive with the graphics previously mentioned. Space for a company logo required. Professional/business application. Company logo already exists, it is blue and red but these colors are not required to be used as a theme.
Industry/Entity Type
Training
Number of Pages Required
1 page
Colors
Designer to choose colors to be used in the design.
Look and feel
Each slider illustrates characteristics of the customer's brand and the style your logo design should communicate.

```html
<!DOCTYPE html>
<html lang="en">
<head>
<meta charset="utf-8">
<title>Veltrano – Research and Development Training</title>
<link rel="stylesheet" href="https://fonts.googleapis.com/css2?family=Montserrat:wght@600;700&family=Open+Sans:ital,wght@0,400;0,600;0,700;1,400&display=swap">
<style>
:root{
  --navy:#1b2167;
  --navy-deep:#0f1650;
  --blue:#1a74c4;
  --red:#e3151d;
  --ink:#1d1d1d;
  --muted:#8a8a8a;
  --line:#dedede;
  --card:#f9f9f9;
  --pale:#f2f3f7;
  --footer:#050b18;
  --white:#ffffff;
}
*{box-sizing:border-box;margin:0;padding:0}
html,body{width:1200px;height:2795px;overflow:hidden}
body{position:relative;background:var(--white);font-family:"Open Sans",Arial,sans-serif;color:var(--ink)}
.abs{position:absolute}

/* hero */
.hero{left:0;top:0;width:1200px;height:640px;
  background:radial-gradient(circle at 230px 520px,#6ec8ff 0,#2a6fd0 12%,rgba(30,60,160,0) 38%),
  radial-gradient(circle at 300px 200px,rgba(230,40,70,.45) 0,rgba(230,40,70,0) 22%),
  linear-gradient(100deg,#1c3f9a 0%,var(--navy) 45%,var(--navy-deep) 100%)}
.nav{left:99px;top:59px;display:flex;gap:45px}
.nav a{color:var(--white);text-decoration:none;font:600 15px "Open Sans",sans-serif;letter-spacing:.2px}
.brand{left:848px;top:44px;display:flex;align-items:center;gap:12px}
.brand-dot{width:40px;height:40px;border-radius:50%;background:var(--blue)}
.brand-name{font:700 32px "Open Sans",sans-serif;color:#2b8ee0}
.hero-title{left:0;top:287px;width:1200px;text-align:center;color:var(--white);
  font:700 43px/1.3 "Montserrat",sans-serif;letter-spacing:.3px}
.dots{left:1143px;top:281px;display:flex;flex-direction:column;gap:15px}
.dots span{width:14px;height:14px;border-radius:50%;border:2px solid var(--white)}
.dots span.on{background:var(--white)}

/* about */
.about{left:0;top:560px;width:1200px;height:300px}
.about h2{position:absolute;top:70px;width:1200px;text-align:center;font:700 27px "Montserrat",sans-serif;color:var(--ink)}
.about p{position:absolute;left:176px;top:112px;width:848px;text-align:center;font:400 12.5px/26px "Open Sans",sans-serif;color:var(--muted)}
.btns{position:absolute;top:208px;width:1200px;display:flex;justify-content:center;gap:8px}
.btn{height:40px;padding:0 26px;border-radius:20px;font:600 14px/36px "Open Sans",sans-serif;border:2px solid var(--blue);color:var(--blue);background:var(--white)}
.btn.solid{background:var(--blue);color:var(--white)}

/* topics */
.card{width:318px;height:252px;background:var(--card);border:1px solid var(--line);text-align:center}
.card-icon{position:absolute;left:106px;top:-52px;width:104px;height:104px;border-radius:50%;background:var(--white);border:1px solid var(--line);display:flex;align-items:center;justify-content:center}
.card-icon i{width:62px;height:62px;border-radius:14px;display:block}
.card h3{margin-top:70px;font:400 21px "Open Sans",sans-serif;color:var(--ink)}
.card p{margin:10px auto 0;width:292px;font:400 13px/22px "Open Sans",sans-serif;color:var(--muted)}
.card .btn{display:inline-block;margin-top:16px;height:38px;line-height:34px;font-size:13.5px;padding:0 18px}

/* testimonial */
.clients{left:0;top:1610px;width:1200px;height:356px;background:linear-gradient(180deg,#1a84d2,#1873c0);color:var(--white);text-align:center}
.clients h2{margin-top:60px;font:700 26px "Montserrat",sans-serif}
.clients blockquote{margin:20px auto 0;width:810px;font:italic 400 14px/26px "Open Sans",sans-serif}
.clients .who{margin-top:12px;font:700 17px "Montserrat",sans-serif}
.stars{color:#f7c325;letter-spacing:2px;margin-left:8px}

/* news */
.news-head{left:99px;top:2018px;width:1001px;display:flex;align-items:center;gap:24px}
.news-head h2{font:700 28px "Montserrat",sans-serif;white-space:nowrap}
.news-head .rule{flex:1;height:1px;background:var(--line)}
.arrow-btn{width:38px;height:38px;border-radius:50%;border:1px solid #cfcfcf;display:flex;align-items:center;justify-content:center}
.post{width:320px}
.post-img{height:210px;position:relative}
.date{position:absolute;left:22px;top:-10px;width:54px;height:62px;background:var(--red);color:var(--white);text-align:center;font:700 14px/1.1 "Montserrat",sans-serif;padding-top:8px}
.date b{display:block;font-size:22px}
.post h3{margin-top:20px;width:285px;font:600 16px/25px "Open Sans",sans-serif;text-transform:uppercase}
.post p{margin-top:10px;font:400 13px/22px "Open Sans",sans-serif;color:var(--muted)}
.meta{margin-top:6px;font:italic 400 12px "Open Sans",sans-serif;color:var(--blue)}

/* footer */
.footer{left:0;top:2500px;width:1200px;height:295px}
.social{left:0;top:2627px;width:1200px;display:flex;justify-content:center;gap:8px}
.social span{width:36px;height:36px;border-radius:50%}
.fnav{left:0;top:2692px;width:1200px;text-align:center;color:var(--white);font:600 13px "Open Sans",sans-serif;word-spacing:3px}
.copy{left:0;top:2729px;width:1200px;text-align:center;color:var(--white);font:400 12.5px "Open Sans",sans-serif}
</style>
</head>
<body>

<div class="abs hero" role="img" aria-label="Technology illustration of glowing circuitry rings and a light beam on deep blue"></div>
<nav class="abs nav"><a>HOME</a><a>ABOUT US</a><a>SERVICES</a><a>REVIEWS</a><a>NEWS</a><a>CONTACT US</a></nav>
<div class="abs brand"><span class="brand-dot"></span><span class="brand-name">Veltrano</span></div>
<h1 class="abs hero-title">RESEARCH AND<br>DEVELOPMENT TRAINING</h1>
<div class="abs dots"><span class="on"></span><span></span><span></span><span></span><span></span></div>

<svg class="abs" style="left:0;top:560px" width="1200" height="300" viewBox="0 0 1200 300">
  <path d="M0 80 Q600 -45 1200 80 V300 H0Z" fill="var(--pale)"/>
</svg>
<section class="abs about">
  <h2>ABOUT LEARNPOINT</h2>
  <p>Sed ut perspiciatis unde omnis iste natus error sit voluptatem accusantium doloremque laudantium, totam rem aperiam, eaque ipsa quae ab illo inventore veritatis et quasi architecto beatae vitae dicta sunt explicabo. Nemo enim ipsam voluptatem quia voluptas sit aspernatur aut odit aut fugit, sed quia consequuntur magni dolores eos qui ratione voluptatem sequi nesciunt. Neque porro quisquam est, qui</p>
  <div class="btns"><span class="btn solid">READ MORE</span><span class="btn">CONTACT US</span></div>
</section>

<div class="abs card" style="left:99px;top:965px"><div class="card-icon"><i role="img" aria-label="Methodology icon of two gears" style="background:linear-gradient(135deg,#f3b21b,#4a5a6a)"></i></div><h3>Methodology</h3><p>Nam libero tempore, cum soluta nobis est eligendi optio cumque nihil impedit quo minus id quod maxime placeat facere possimus</p><span class="btn">READ MORE</span></div>
<div class="abs card" style="left:441px;top:965px"><div class="card-icon"><i role="img" aria-label="Equipment icon of a rising bar chart" style="background:linear-gradient(135deg,#2d7fd0,#f4a623)"></i></div><h3>Equipment</h3><p>Nam libero tempore, cum soluta nobis est eligendi optio cumque nihil impedit quo minus id quod maxime placeat facere possimus</p><span class="btn">READ MORE</span></div>
<div class="abs card" style="left:781px;top:965px"><div class="card-icon"><i role="img" aria-label="Design references icon of a framed chip" style="background:linear-gradient(135deg,#d9534f,#3c8d3c)"></i></div><h3>Design References</h3><p>Nam libero tempore, cum soluta nobis est eligendi optio cumque nihil impedit quo minus id quod maxime placeat facere possimus</p><span class="btn">READ MORE</span></div>
<div class="abs card" style="left:99px;top:1299px"><div class="card-icon"><i role="img" aria-label="Safety icon of a padlock" style="background:linear-gradient(135deg,#f5c431,#e0a70f)"></i></div><h3>Safety &amp; Environmental</h3><p>Nam libero tempore, cum soluta nobis est eligendi optio cumque nihil impedit quo minus id quod maxime placeat facere possimus</p><span class="btn">READ MORE</span></div>
<div class="abs card" style="left:441px;top:1299px"><div class="card-icon"><i role="img" aria-label="Technology icon of a computer monitor" style="background:linear-gradient(135deg,#e6504a,#5a6a7a)"></i></div><h3>Technology</h3><p>Nam libero tempore, cum soluta nobis est eligendi optio cumque nihil impedit quo minus id quod maxime placeat facere possimus</p><span class="btn">READ MORE</span></div>

<section class="abs clients">
  <h2>WHAT CLIENTS SAY</h2>
  <svg width="60" height="48" viewBox="0 0 60 48" style="margin-top:20px"><path d="M4 44V26Q4 8 22 4M32 44V26Q32 8 50 4M4 26H22V44H4M32 26H50V44H32" fill="none" stroke="#fff" stroke-width="2"/></svg>
  <blockquote>At vero eos et accusamus et iusto odio dignissimos ducimus qui blanditiis praesentium voluptatum deleniti atque corrupti quos dolores et quas molestias excepturi sint occaecati cupiditate non provident, similique sunt in culpa qui officia deserunt mollitia animi, id est laborum et harum quidem rerum facilis est et expedita distinctio.</blockquote>
  <div class="who">- OFFICIIS DEBITIS<span class="stars">★★★★★</span></div>
  <svg class="abs" style="left:68px;top:140px" width="36" height="70"><path d="M34 2 2 35 34 68" fill="none" stroke="#fff" stroke-width="2"/></svg>
  <svg class="abs" style="left:1096px;top:140px" width="36" height="70"><path d="M2 2 34 35 2 68" fill="none" stroke="#fff" stroke-width="2"/></svg>
</section>

<div class="abs news-head"><h2>LATEST NEWS</h2><span class="rule"></span>
  <span class="arrow-btn"><svg width="10" height="14"><path d="M8 1 2 7 8 13" fill="none" stroke="#222" stroke-width="2"/></svg></span>
  <span class="arrow-btn" style="margin-left:-16px"><svg width="10" height="14"><path d="M2 1 8 7 2 13" fill="none" stroke="#222" stroke-width="2"/></svg></span>
</div>
<article class="abs post" style="left:99px;top:2087px"><div class="post-img" role="img" aria-label="Laboratory research photo with flask and gears" style="background:linear-gradient(120deg,#e0218a,#7a3bd1 50%,#2a3a8a)"><span class="date">MAR<b>20</b></span></div><h3>Culpa qui officia deserunt mollitia anim</h3><p>At vero eos et accusamus et iusto odio dignissimos ducimus qui blanditiis praesentium..</p><div class="meta">By Admin &nbsp;|&nbsp; Comments</div></article>
<article class="abs post" style="left:440px;top:2087px"><div class="post-img" role="img" aria-label="Data analytics photo with glowing charts" style="background:radial-gradient(circle at 50% 55%,#f0a030,#c8302a 30%,#1b2a22 75%)"><span class="date">MAR<b>20</b></span></div><h3>Culpa qui officia deserunt mollitia anim</h3><p>At vero eos et accusamus et iusto odio dignissimos ducimus qui blanditiis praesentium..</p><div class="meta">By Admin &nbsp;|&nbsp; Comments</div></article>
<article class="abs post" style="left:780px;top:2087px"><div class="post-img" role="img" aria-label="Technology photo of a light beam over blue circuitry" style="background:radial-gradient(circle at 40% 80%,#9ad8ff,#2366c8 25%,#0c1c5c 70%)"><span class="date">MAR<b>20</b></span></div><h3>Culpa qui officia deserunt mollitia anim</h3><p>At vero eos et accusamus et iusto odio dignissimos ducimus qui blanditiis praesentium..</p><div class="meta">By Admin &nbsp;|&nbsp; Comments</div></article>

<svg class="abs footer" viewBox="0 0 1200 295"><path d="M0 0 Q600 120 1200 0 V295 H0Z" fill="var(--footer)"/></svg>
<div class="abs social">
  <span style="background:#1a6fbf"></span><span style="background:#3a5296"></span><span style="background:#2aa3e6"></span><span style="background:#6a3a2c"></span><span style="background:#d8342a"></span><span style="background:#d81f2b"></span><span style="background:#f06a2a"></span><span style="background:#e0201d"></span>
</div>
<div class="abs fnav">HOME &nbsp;|&nbsp; ABOUT US &nbsp;|&nbsp; SERVICES &nbsp;|&nbsp; NEWS &nbsp;|&nbsp; REVIEWS &nbsp;|&nbsp; CONTACT US</div>
<div class="abs copy">Copyrights © 2018 Veltrano.All rights reserved. &nbsp;|&nbsp; Privacy policy</div>

</body>
</html>
```